Brightway Haul & Repair Services, are a company that offers a 'one stop shop' pre-move clean up a

I have already selected a logo which I would like on the front of the business cards along with phone numbers, web address and email which are:
0419574302
www.brightwayhaul.com.au
brightwayhaulrepair@mailbox.example

On the back of the card I would like to list some of the types of service we offer (clean - move - repairs/maintenance) which are:
CLEAN - windows, gutters, solar panels, driveways/paths, carpets.
MOVE - Small/medium size house/office moves, large item pick-up & delivery, yard clean-up and removal.
General maintenance and repairs.

I would like the blue logo on a gray background.

Thanks

```html
<!DOCTYPE html>
<html lang="en">
<head>
<meta charset="utf-8">
<title>Brightway Haul &amp; Repair Services – Services Card</title>
<link rel="stylesheet" href="https://fonts.googleapis.com/css2?family=Arimo:wght@400&family=Passion+One:wght@700&display=swap">
<style>
  :root {
    --card-grey: #808080;
    --ink-black: #000000;
    --clean-blue: #72b4d8;
    --list-blue: #6cb0d6;
    --move-white: #ffffff;
    --footer-blue: #22609f;
  }
  html, body {
    margin: 0;
    padding: 0;
    width: 1200px;
    height: 734px;
    overflow: hidden;
    background: var(--card-grey);
  }
  .services-card {
    display: block;
    width: 1200px;
    height: 734px;
  }
  .card-background { fill: var(--card-grey); }
  .intro {
    font-family: "Arimo", Arial, sans-serif;
    font-size: 39px;
    fill: var(--ink-black);
  }
  .category-heading {
    font-family: "Passion One", "Arial Black", sans-serif;
    font-weight: 700;
    font-size: 132px;
    letter-spacing: 2px;
  }
  .category-heading--clean { fill: var(--clean-blue); }
  .category-heading--move { fill: var(--move-white); }
  .service-list {
    font-family: "Arimo", Arial, sans-serif;
    font-size: 56px;
  }
  .service-list--clean { fill: var(--list-blue); }
  .service-list--move { fill: var(--move-white); font-size: 54px; }
  .maintenance-line {
    font-family: "Arimo", Arial, sans-serif;
    font-size: 50px;
    fill: var(--footer-blue);
  }
</style>
</head>
<body>
<svg class="services-card" viewBox="0 0 1200 734" xmlns="http://www.w3.org/2000/svg" role="group" aria-label="Brightway Haul &amp; Repair Services – services we offer">
  <rect class="card-background" x="0" y="0" width="1200" height="734"/>

  <text class="intro" x="38" y="66">We can:</text>

  <text class="category-heading category-heading--clean" x="284" y="203" text-anchor="middle" textLength="428" lengthAdjust="spacingAndGlyphs">CLEAN</text>
  <text class="category-heading category-heading--move" x="868" y="203" text-anchor="middle" textLength="354" lengthAdjust="spacingAndGlyphs">MOVE</text>

  <g class="service-list service-list--clean" text-anchor="middle">
    <text x="297" y="271">windows</text>
    <text x="297" y="356">gutters</text>
    <text x="297" y="441">solar panels</text>
    <text x="297" y="526">driveways/paths</text>
    <text x="297" y="610">carpets</text>
  </g>

  <g class="service-list service-list--move" text-anchor="middle">
    <text x="868" y="271">small to medium-sized</text>
    <text x="868" y="320">home/office moves</text>
    <text x="868" y="417">large item pick-up/</text>
    <text x="868" y="466">delivery</text>
    <text x="868" y="564">yard clean-up and</text>
    <text x="868" y="613">removal</text>
  </g>

  <text class="maintenance-line" x="608" y="692" text-anchor="middle">Perform general maintenance and repairs</text>
</svg>
</body>
</html>
```